Rack Card for Harbor Lens Studios

Looking to make a verticle rack card back and front 3.5 X 8.5, add .125 on each side for bleed, CMYK, need .psd file and all fonts. We are based out of Connecticut but we are adding a location in Florida so it needs to be beach themed. I have a sample photo image but something else could be used. Front side should have image, logo, back side should have pricing. For your reference our Connecticut site is www.hlsbridalfilms.com but the Florida site will be
www.hlsgc.com
941-555-0127

Target Market(s)

Brides

Industry/Entity Type

Wedding Photography

Requirements
Must have
• Beach theme

```html
<!DOCTYPE html>
<html lang="en">
<head>
<meta charset="utf-8">
<title>Harbor Lens Studios – Rack Card</title>
<link rel="stylesheet" href="https://fonts.googleapis.com/css2?family=Open+Sans:wght@400;600&family=Roboto+Condensed:wght@400&display=swap">
<style>
  :root{
    --stage:#dcdcdc;
    --white:#ffffff;
    --navy:#1d3f86;
    --ink:#1a2a4a;
    --blue:#2f7cc6;
    --blue-deep:#1f63b3;
    --blue-light:#3f8fd2;
    --sky:#a9d8f5;
    --pill-text:#1d4f8f;
    --phone:#3b4fa0;
  }
  *{margin:0;padding:0;box-sizing:border-box}
  html,body{width:1200px;height:1157px;overflow:hidden;background:var(--stage)}
  .stage{position:relative;width:1200px;height:1157px}
  .card{position:absolute;top:68px;width:434px;height:1012px;background:var(--white);overflow:hidden}
  .card--front{left:116px}
  .card--back{left:639px}
  .card-art{position:absolute;inset:0;width:434px;height:1012px}
  .brand{position:absolute;display:flex;align-items:center;gap:10px;
    font-family:"Open Sans",sans-serif;font-weight:600;color:var(--navy);font-size:27px;line-height:1}
  .brand-dot{width:26px;height:26px;border-radius:50%;background:var(--blue-deep);flex:none}
  .card--front .brand{top:58px;left:0;right:0;justify-content:center}
  .card--back .brand{top:58px;left:30px;font-size:24px}
  .tagline{position:absolute;left:0;right:0;top:818px;text-align:center;color:var(--white);
    font-family:"Roboto Condensed",sans-serif;font-size:20.5px;line-height:29px;letter-spacing:.2px}
  .contact{position:absolute;left:0;right:0;top:936px;text-align:center;color:var(--phone);
    font-family:"Open Sans",sans-serif}
  .contact-phone{display:flex;justify-content:center;align-items:center;gap:4px;font-size:26px;letter-spacing:1.5px;line-height:32px}
  .contact-phone svg{width:20px;height:20px}
  .contact-web{font-size:21px;letter-spacing:1px;line-height:28px}
  .pill{position:absolute;left:0;width:293px;height:37px;background:var(--sky);
    border-radius:0 19px 19px 0;color:var(--pill-text);font-family:"Open Sans",sans-serif;
    font-size:18px;line-height:37px;padding-left:21px}
  .list{position:absolute;left:18px;right:14px;list-style:none;color:var(--white);
    font-family:"Open Sans",sans-serif;font-size:14.6px;line-height:19.2px}
  .list li{padding-left:12px;position:relative}
  .list li::before{content:"•";position:absolute;left:0}
  .note{position:absolute;left:24px;color:var(--white);font-family:"Open Sans",sans-serif;font-size:14.6px;line-height:19.2px}
</style>
</head>
<body>
<div class="stage">

  <!-- FRONT -->
  <section class="card card--front">
    <svg class="card-art" viewBox="0 0 434 1012" aria-hidden="false">
      <defs>
        <linearGradient id="beach" x1="0" y1="0" x2="0" y2="1">
          <stop offset="0" stop-color="#dfe6ec"/>
          <stop offset=".38" stop-color="#c9d7df"/>
          <stop offset=".48" stop-color="#a8bcc4"/>
          <stop offset=".58" stop-color="#d8c9b2"/>
          <stop offset="1" stop-color="#c9b397"/>
        </linearGradient>
        <linearGradient id="frontBlue" x1="0" y1="0" x2="1" y2="1">
          <stop offset="0" stop-color="var(--blue-deep)"/>
          <stop offset="1" stop-color="var(--blue-light)"/>
        </linearGradient>
      </defs>
      <path role="img" aria-label="Photo: bride and groom on a beach with a white orchid bouquet in the sand"
        fill="url(#beach)"
        d="M0,170 C70,205 160,200 240,175 C320,150 390,140 434,175 L434,760 C390,720 310,705 230,735 C150,765 60,745 20,700 C8,685 2,670 0,655 Z"/>
      <path fill="var(--blue-deep)" d="M0,132 C25,185 130,205 240,178 C310,160 380,140 434,158 L434,172 C380,150 310,170 240,192 C130,222 25,205 0,168 Z"/>
      <path fill="var(--sky)" d="M240,178 C310,158 390,135 434,150 L434,250 C420,195 380,165 300,172 Z"/>
      <path fill="var(--sky)" d="M0,655 C10,700 80,760 200,745 C290,735 380,700 434,730 L434,760 C380,730 300,750 210,770 C90,795 10,740 0,700 Z"/>
      <path fill="var(--white)" d="M0,700 C10,745 90,795 210,770 C300,752 380,732 434,760 L434,780 C380,755 300,770 210,795 C90,825 15,790 0,760 Z"/>
      <path fill="url(#frontBlue)" d="M0,760 C15,790 90,825 210,795 C300,770 380,755 434,780 L434,1012 L0,1012 Z"/>
      <path fill="none" stroke="var(--sky)" stroke-width="4" d="M60,935 C170,905 300,905 400,932"/>
      <path fill="var(--white)" d="M0,950 C120,915 310,912 434,950 L434,1012 L0,1012 Z"/>
    </svg>
    <div class="brand"><span class="brand-dot"></span>Harbor Lens Studios</div>
    <p class="tagline">UNOBTRUSIVE • DOCUMENTARY • CINEMATIC<br>WEDDING VIDEOGRAPHY</p>
    <div class="contact">
      <div class="contact-phone"><svg viewBox="0 0 24 24"><circle cx="12" cy="12" r="10.5" fill="none" stroke="currentColor" stroke-width="1.8"/><path fill="currentColor" d="M8.6 6.5l1.6-.4 1.2 2.8-1.1 1a7 7 0 0 0 3.8 3.8l1-1.1 2.8 1.2-.4 1.6c-.2.7-.9 1-1.6.9A9 9 0 0 1 7.7 8.1c-.1-.7.2-1.4.9-1.6z"/></svg>941-555-0127</div>
      <div class="contact-web">www.hlsgc.com</div>
    </div>
  </section>

  <!-- BACK -->
  <section class="card card--back">
    <svg class="card-art" viewBox="0 0 434 1012">
      <defs>
        <linearGradient id="backBlue" x1="0" y1="0" x2="1" y2="1">
          <stop offset="0" stop-color="var(--blue-deep)"/>
          <stop offset=".6" stop-color="var(--blue)"/>
          <stop offset="1" stop-color="var(--blue-light)"/>
        </linearGradient>
      </defs>
      <path fill="url(#backBlue)" d="M0,150 C30,200 130,215 250,190 C330,172 390,160 434,175 L434,1012 L0,1012 Z"/>
      <path fill="var(--white)" d="M0,178 C40,215 140,222 250,198 C330,180 390,170 434,182 L434,190 C390,178 330,188 250,206 C140,230 40,225 0,195 Z"/>
      <path fill="var(--blue-deep)" d="M0,195 C40,225 140,230 250,206 C330,188 390,178 434,190 L434,200 C390,190 330,200 250,218 C140,242 40,235 0,210 Z" opacity=".6"/>
      <path fill="var(--sky)" d="M160,200 C240,185 320,165 434,170 L434,176 C330,172 250,192 170,208 Z"/>
      <path fill="#4f9ad8" d="M305,0 L421,0 L421,232 L363,222 L305,232 Z"/>
      <path fill="none" stroke="var(--sky)" stroke-width="4" d="M60,935 C170,905 300,905 400,932"/>
      <path fill="var(--white)" d="M0,950 C120,915 310,912 434,950 L434,1012 L0,1012 Z"/>
    </svg>
    <div class="brand"><span class="brand-dot"></span>Harbor Lens Studios</div>

    <div class="pill" style="top:232px">All Packages include:</div>
    <ul class="list" style="top:276px">
      <li>Broadcast Quality Equipment shot in HD</li>
      <li>Personalized DVD</li>
      <li>Remote Microphone for clear audio</li>
      <li>Professional editing</li>
    </ul>
    <p class="note" style="top:370px">Ceremony Only Coverage - $399</p>
    <ul class="list" style="top:389px;left:26px"><li>Up to 1 hour of coverage.</li></ul>

    <div class="pill" style="top:424px">Classic Package - $999</div>
    <ul class="list" style="top:472px">
      <li>Up to 5 hours of coverage.</li>
      <li>Background music where suitable.</li>
      <li>Names of the bridal party and family.</li>
    </ul>

    <div class="pill" style="top:546px">Deluxe Package - $1299</div>
    <ul class="list" style="top:595px">
      <li>Up to 6 hours of coverage.</li>
      <li>Background music where suitable.</li>
      <li>Names of the bridal party and family.</li>
      <li>An online recap of the wedding highlights edited to your song choice.</li>
      <li>Two extra DVD copies in custom cases.</li>
    </ul>

    <div class="pill" style="top:728px">Extras</div>
    <ul class="list" style="top:776px">
      <li>Hourly Coverage $100/hour</li>
      <li>DVD Copy $25</li>
      <li>Blu Ray Copy $50</li>
      <li>Photo Montage up to 25 photos $150</li>
      <li>Drone Aerial Coverage $250/hour</li>
      <li>Entire Wedding on the Cloud $100</li>
    </ul>

    <div class="contact">
      <div class="contact-phone"><svg viewBox="0 0 24 24"><circle cx="12" cy="12" r="10.5" fill="none" stroke="currentColor" stroke-width="1.8"/><path fill="currentColor" d="M8.6 6.5l1.6-.4 1.2 2.8-1.1 1a7 7 0 0 0 3.8 3.8l1-1.1 2.8 1.2-.4 1.6c-.2.7-.9 1-1.6.9A9 9 0 0 1 7.7 8.1c-.1-.7.2-1.4.9-1.6z"/></svg>941-555-0127</div>
      <div class="contact-web">www.hlsgc.com</div>
    </div>
  </section>

</div>
</body>
</html>
```